Detail Shop Business card design

i need a business card design for my new detailing company called 'Brenner's Detail Shop'. i want an all black and white design . simple, direct and to the point. i want the designer to choose a fitting font to match the logothe front should have logo, address, phone and email and the back side should have a slogan and text indicating that we offer services on anything including cars, trucks, motorcycles and RVs. slogan will read "we take pride in your ride"
maybe also very small on the back side the IG icon with Brenners_Detail_Shop

phone 482.615.7734
address 7384 E Harlow Ave
Spokane WA 99342
email: BrennersDetail@quorvail.com

Target Market(s)

all ages , auto enthusiasts

Industry/Entity Type

Automotive

Contact Information for Business Card

the front should have logo, address, phone and email and the back side should have a slogan and text indicating that we offer services on anything including cars, trucks, motorcycles and RVs. slogan will read "we take pride in your ride"

phone 482.615.7734
address 7384 E Harlow Ave
Spokane WA 99342

Colors
000000
ffffff

Requirements
Must have
• bold font and very simple design with good spacing
Nice to have
• anything creative from the designer indicating we service any types of vehicles
Should not have
• any colors ,

```html
<!DOCTYPE html>
<html lang="en">
<head>
<meta charset="utf-8">
<title>Brenner's Detail Shop — Business Card</title>
<link href="https://fonts.googleapis.com/css2?family=Oswald:wght@500;700&family=Open+Sans:wght@400&display=swap" rel="stylesheet">
<style>
  :root {
    --canvas: #dedede;
    --card: #0b0b0b;
    --ink: #ffffff;
    --gloss: #2a2a2a;
    --gloss-text: #1d1d1d;
  }
  * { box-sizing: border-box; margin: 0; padding: 0; }
  html, body { width: 1200px; height: 900px; overflow: hidden; }
  body {
    background: var(--canvas);
    display: flex;
    flex-direction: column;
    align-items: center;
    justify-content: center;
    gap: 56px;
  }
  .card {
    width: 630px;
    height: 360px;
    background: var(--card);
    border-radius: 26px;
    position: relative;
    overflow: hidden;
    color: var(--ink);
  }
  .brand {
    font-family: "Oswald", sans-serif;
    font-weight: 700;
    text-transform: uppercase;
    letter-spacing: 2px;
    display: flex;
    align-items: center;
    gap: 12px;
    position: absolute;
    left: 50%;
    transform: translateX(-50%);
    white-space: nowrap;
  }
  .brand-dot {
    width: 14px; height: 14px; border-radius: 50%;
    background: currentColor;
  }
  .card-front .brand { top: 80px; font-size: 34px; color: var(--ink); }
  .contact {
    position: absolute;
    left: 36px; right: 36px; bottom: 62px;
    font-family: "Open Sans", sans-serif;
    font-size: 14px;
    display: grid;
    grid-template-columns: max-content max-content;
    column-gap: 36px;
    row-gap: 14px;
    justify-content: center;
  }
  .contact-item { display: flex; align-items: center; gap: 8px; white-space: nowrap; }
  .contact-item svg { width: 15px; height: 15px; flex: none; }
  .handle-mark { width: 13px; height: 13px; border: 2px solid var(--ink); border-radius: 3px; flex: none; }

  .card-back .brand { top: 80px; font-size: 34px; color: var(--gloss); }
  .back-copy {
    position: absolute;
    left: 0; right: 0; top: 190px;
    text-align: center;
    font-family: "Oswald", sans-serif;
    text-transform: uppercase;
    color: var(--gloss-text);
  }
  .slogan { font-size: 20px; font-weight: 700; letter-spacing: 1px; }
  .services { font-size: 22px; font-weight: 500; letter-spacing: 1.5px; margin-top: 12px; }
</style>
</head>
<body>
  <section class="card card-front">
    <div class="brand"><span class="brand-dot"></span>Brenner's Detail Shop</div>
    <div class="contact">
      <div class="contact-item">
        <svg viewBox="0 0 16 16" aria-hidden="true"><path fill="#fff" d="M3 2h3l1 3-2 1a9 9 0 0 0 5 5l1-2 3 1v3a1 1 0 0 1-1 1A13 13 0 0 1 2 3a1 1 0 0 1 1-1z"/></svg>
        482.615.7734
      </div>
      <div class="contact-item">
        <svg viewBox="0 0 16 16" aria-hidden="true"><path fill="#fff" d="M8 1a5 5 0 0 0-5 5c0 4 5 9 5 9s5-5 5-9a5 5 0 0 0-5-5zm0 7a2 2 0 1 1 0-4 2 2 0 0 1 0 4z"/></svg>
        7384 E Harlow Ave, Spokane WA 99342
      </div>
      <div class="contact-item">
        <svg viewBox="0 0 16 16" aria-hidden="true"><rect x="1" y="3" width="14" height="10" fill="#fff"/><path d="M1 3l7 6 7-6" fill="none" stroke="#0b0b0b" stroke-width="1.4"/></svg>
        BrennersDetail@quorvail.com
      </div>
      <div class="contact-item">
        <span class="handle-mark"></span>
        Brenners_Detail_Shop
      </div>
    </div>
  </section>

  <section class="card card-back">
    <div class="brand"><span class="brand-dot"></span>Brenner's Detail Shop</div>
    <div class="back-copy">
      <p class="slogan">We take #prideinyourride</p>
      <p class="services">Cars | Trucks | Motorcycles | RVs</p>
    </div>
  </section>
</body>
</html>
```